Varnel Health new year card

Hi,
I would like a New Year greetings card to send to my customers.

If you need to look at our logo : www.varnelhealth.com

If you want to play with images of our device, see
qirtatherapy.ca

The goal is to have a card to wish a happy new year and we look forward collaborating with them in the new year.

```html
<!DOCTYPE html>
<html lang="en">
<head>
<meta charset="utf-8">
<title>Varnel Health – New Year Card</title>
<link rel="stylesheet" href="https://fonts.googleapis.com/css2?family=Josefin+Slab:wght@300;400&family=Barlow:wght@400;500;600&display=swap">
<style>
  :root {
    --backdrop: #262626;
    --paper: #ffffff;
    --brick: #c1412b;
    --tangerine: #f07a25;
    --ink: #1f1f1f;
    --slate: #5a5b5e;
  }
  * { box-sizing: border-box; margin: 0; padding: 0; }
  html, body {
    width: 1200px; height: 1200px; overflow: hidden;
    background: var(--backdrop);
  }
  .card {
    position: absolute; left: 304px; top: 180px;
    width: 592px; height: 840px;
    background: var(--paper);
  }
  .card__frame {
    position: absolute; left: 20px; top: 18px;
    width: 551px; height: 804px;
    border: 2px solid var(--brick);
  }
  .greeting {
    position: absolute; left: 0; right: 0; top: 44px;
    text-align: center;
    font-family: "Josefin Slab", serif;
    font-weight: 400; line-height: 1;
  }
  .greeting__title { display: block; font-size: 44px; color: var(--brick); letter-spacing: 1px; }
  .greeting__year { display: block; margin-top: 8px; font-size: 42px; color: var(--tangerine); letter-spacing: 1px; }
  .device-photo {
    position: absolute; left: 256px; top: 178px;
    width: 80px; height: 92px; border-radius: 14px;
    background: linear-gradient(160deg, #e9ecef, #b8bec4);
  }
  .tree-graphic {
    position: absolute; left: 126px; top: 268px;
    width: 342px; height: 392px;
  }
  .message {
    position: absolute; left: 0; right: 0; top: 672px;
    text-align: center;
    font-family: "Barlow", sans-serif; font-weight: 400;
    font-size: 18px; color: var(--ink);
  }
  .brand {
    position: absolute; left: 0; right: 0; top: 740px;
    display: flex; justify-content: center; align-items: center; gap: 8px;
  }
  .brand__square { width: 14px; height: 14px; background: var(--tangerine); }
  .brand__name {
    font-family: "Barlow", sans-serif; font-weight: 600;
    font-size: 22px; color: var(--slate);
  }
  .web-banner {
    position: absolute; left: 166px; top: 786px;
    width: 260px; height: 34px;
  }
  .web-banner__text {
    position: absolute; inset: 0;
    display: flex; align-items: center; justify-content: center;
    font-family: "Barlow", sans-serif; font-weight: 500;
    font-size: 16px; color: var(--paper);
  }
</style>
</head>
<body>
  <main class="card">
    <div class="card__frame"></div>

    <h1 class="greeting">
      <span class="greeting__title">Happy New Year</span>
      <span class="greeting__year">2022</span>
    </h1>

    <div class="device-photo" role="img" aria-label="Photo of the Varnel Health therapy device with its cable"></div>

    <svg class="tree-graphic" viewBox="0 0 342 392" role="img" aria-label="Graphic of a festive tree built from orange and red slanted bars">
      <defs>
        <linearGradient id="treeTone" x1="0" y1="0" x2="1" y2="1">
          <stop offset="0" stop-color="#f07a25"/>
          <stop offset="1" stop-color="#c1412b"/>
        </linearGradient>
      </defs>
      <polygon points="171,0 342,392 0,392" fill="url(#treeTone)" opacity="0.9"/>
    </svg>

    <p class="message">We look forward collaborating with you in the new year.</p>

    <div class="brand">
      <span class="brand__square"></span>
      <span class="brand__name">Varnel Health</span>
    </div>

    <div class="web-banner">
      <svg width="260" height="34" viewBox="0 0 260 34" aria-hidden="true">
        <polygon points="14,0 246,0 260,34 0,34" fill="#e0542a"/>
      </svg>
      <span class="web-banner__text">www.varnelhealth.com</span>
    </div>
  </main>
</body>
</html>
```